I want to revise my business card design and get a more modern and up to date design.

Brolvane Handyman Sevices originated from a family-owned and operated contractor business, performing home renovation, addition, and construction work in the NYC area since 2004. Today, we specialize in reliable and affordable handyman services for residential and commercial clients In 2014, we expanded to northern New Jersey. In 2016, we brought quality home improvement and repair services to new Bucks County, PA, and nearby New Jersey areas.
Target Market(s)
Home owners and business that might be looking for a General contractor, handyman, cleaning services and Home maintenance and property.
Industry/Entity Type
Construction Company
Contact Information for Business Card
I am open to new ideas
Colors
Designer to choose colors to be used in the design.
Look and feel
Each slider illustrates characteristics of the customer's brand and the style your logo design should communicate.

```html
<!DOCTYPE html>
<html lang="en">
<head>
<meta charset="utf-8">
<title>Brolvane Handyman Sevices – Business Card</title>
<link rel="stylesheet" href="https://fonts.googleapis.com/css2?family=Montserrat:wght@500;600;700;800&family=Open+Sans:wght@400;600&display=swap">
<style>
  :root {
    --page-bg: #d9d9d9;
    --card-bg: #2f2f30;
    --card-edge: #3a3a3b;
    --brand-red: #e5202b;
    --text-white: #ffffff;
    --text-grey: #8a8a8a;
    --divider: #e5202b;
  }
  * { box-sizing: border-box; margin: 0; padding: 0; }
  html, body {
    width: 1200px; height: 1000px; overflow: hidden;
    background: var(--page-bg);
  }
  .sheet {
    width: 1200px; height: 1000px;
    display: flex; flex-direction: column;
    align-items: center; justify-content: center; gap: 44px;
  }
  .card {
    width: 760px; height: 430px;
    background: linear-gradient(160deg, var(--card-edge), var(--card-bg) 60%);
    border-radius: 26px;
    position: relative;
    font-family: "Montserrat", sans-serif;
    color: var(--text-white);
  }

  /* Wordmark */
  .wordmark {
    display: flex; align-items: center; gap: 14px;
  }
  .wordmark-square {
    width: 30px; height: 30px; background: var(--brand-red);
  }
  .wordmark-name {
    font-weight: 800; color: var(--brand-red);
    letter-spacing: -1px; line-height: 1;
  }
  .wordmark-tagline {
    font-family: "Open Sans", sans-serif;
    color: var(--text-grey);
    letter-spacing: 4px; text-transform: uppercase;
  }

  /* Front */
  .card-front {
    display: flex; flex-direction: column;
    align-items: center; justify-content: center;
  }
  .card-front .wordmark-name { font-size: 78px; }
  .card-front .wordmark-tagline { font-size: 17px; margin-top: 10px; letter-spacing: 6px; }
  .service-list {
    margin-top: 34px; display: flex; align-items: center; gap: 10px;
    font-weight: 700; font-size: 15px; letter-spacing: 0.5px;
  }
  .service-list .marker {
    width: 9px; height: 9px; background: var(--brand-red); display: inline-block;
  }

  /* Back */
  .card-back .identity {
    position: absolute; left: 60px; top: 110px;
    display: flex; align-items: center;
  }
  .card-back .brand-block { display: flex; flex-direction: column; align-items: flex-end; }
  .card-back .wordmark-square { width: 22px; height: 22px; }
  .card-back .wordmark-name { font-size: 54px; }
  .card-back .wordmark-tagline { font-size: 12px; margin-top: 6px; }
  .divider {
    width: 2px; height: 120px; background: var(--divider); margin: 0 26px;
  }
  .contact-name {
    color: var(--brand-red); font-weight: 700; font-size: 22px; margin-bottom: 10px;
  }
  .contact-line {
    display: flex; align-items: center; gap: 8px;
    font-family: "Open Sans", sans-serif; font-size: 15px; margin-top: 4px;
  }
  .contact-line svg { width: 12px; height: 12px; fill: var(--brand-red); flex: none; }
  .card-back .summary {
    position: absolute; left: 60px; right: 60px; top: 300px;
    font-weight: 700; font-size: 15px;
  }
  .pillars {
    display: flex; align-items: center; gap: 12px;
    margin-top: 8px; margin-left: 86px;
    font-weight: 700; font-size: 17px; letter-spacing: 0.5px;
  }
  .pillars .dot {
    width: 9px; height: 9px; border-radius: 50%; background: var(--brand-red);
  }
</style>
</head>
<body>
<main class="sheet">

  <section class="card card-front" aria-label="Business card front">
    <div class="wordmark">
      <span class="wordmark-square"></span>
      <span class="wordmark-name">Brolvane</span>
    </div>
    <div class="wordmark-tagline">Handyman Services</div>
    <div class="service-list">
      <span>PROPERTY</span><span class="marker"></span>
      <span>MAINTENANCE</span><span class="marker"></span>
      <span>LANDSCAPE</span><span class="marker"></span>
      <span>CLEANING</span>
    </div>
  </section>

  <section class="card card-back" aria-label="Business card back">
    <div class="identity">
      <div class="brand-block">
        <div class="wordmark">
          <span class="wordmark-square"></span>
          <span class="wordmark-name">Brolvane</span>
        </div>
        <div class="wordmark-tagline">Handyman Services</div>
      </div>
      <div class="divider"></div>
      <div class="contact">
        <div class="contact-name">Marcus Delano</div>
        <div class="contact-line">
          <svg viewBox="0 0 24 24" aria-hidden="true"><path d="M6.6 10.8a15 15 0 0 0 6.6 6.6l2.2-2.2a1 1 0 0 1 1-.25 11.4 11.4 0 0 0 3.6.57 1 1 0 0 1 1 1V20a1 1 0 0 1-1 1A17 17 0 0 1 3 4a1 1 0 0 1 1-1h3.5a1 1 0 0 1 1 1c0 1.25.2 2.45.57 3.57a1 1 0 0 1-.25 1z"/></svg>
          <span>(215) 555 -0192</span>
        </div>
        <div class="contact-line">
          <svg viewBox="0 0 24 24" aria-hidden="true"><path d="M2 5h20v14H2z M2 5l10 8 10-8" /></svg>
          <span>brolvanehandymannyc@mail.com</span>
        </div>
      </div>
    </div>
    <div class="summary">
      <p>General contractor, Property Maintenance, Cleaning and Handyman Services</p>
      <div class="pillars">
        <span>REPAIR</span><span class="dot"></span>
        <span>IMPROVE</span><span class="dot"></span>
        <span>MAINTAIN</span><span class="dot"></span>
        <span>REMODEL</span>
      </div>
    </div>
  </section>

</main>
</body>
</html>
```